DNN Website Design Project

We are going to recreate the website www.plorvenstudio.com. This is a DNN website. We like http://www.quilbarnhq.com/ and something like http://www.redstonequarryweb.com/

Look at plorvenstudio.com to see what we do, SMM, SEO and website development mostly. We have a number of video testimonials and want people to be able to contact us easily and have social media integration.

Target Market(s)

small and medium sized business owners, doctors, private practice professionals, lawyers, service pros (plumbers, electricians)

Industry/Entity Type

Media

```html
<!DOCTYPE html>
<html lang="en">
<head>
<meta charset="utf-8">
<title>Plorven Studio, Inc.</title>
<link href="https://fonts.googleapis.com/css2?family=Ubuntu:wght@400;500;700&family=PT+Sans:ital,wght@0,400;0,700;1,400;1,700&family=Arimo:wght@400;700&display=swap" rel="stylesheet">
<style>
:root{
  --red:#d0121a;
  --green:#5a9e1c;
  --navy:#1b2a45;
  --navy-deep:#0d1626;
  --body-text:#555;
  --line:#e2e2e2;
  --footer:#141b29;
  --bottom:#060709;
  --orange:#f0841e;
  --brand-text:#2a2a2a;
}
*{margin:0;padding:0;box-sizing:border-box}
html,body{width:721px;height:1200px;overflow:hidden}
body{position:relative;background:#f6f7f8;font-family:"Arimo",Arial,sans-serif;color:var(--body-text)}
.abs{position:absolute}
a{color:inherit;text-decoration:none}

/* header */
.site-header{left:0;top:0;width:721px;height:72px;background:#fff}
.top-links{left:447px;top:0;height:14px;width:186px;background:#2a2a2a;border-radius:0 0 8px 8px;display:flex;align-items:center;font-size:7px;color:#ddd;letter-spacing:.4px;overflow:hidden}
.top-links span{padding:0 6px;border-right:1px solid #555}
.top-links .login{margin-left:auto;background:var(--red);color:#fff;height:14px;display:flex;align-items:center;padding:0 14px;border:none}
.brand{left:85px;top:20px}
.brand-name{font-family:"Ubuntu",sans-serif;font-weight:400;font-size:17px;line-height:18px;color:var(--brand-text)}
.social{top:32px;display:block;width:21px;height:21px;border-radius:50%;background:#3b78b5}

/* nav */
.main-nav{left:0;top:72px;width:721px;height:31px;background:linear-gradient(#fafafa,#e8e8e8);border-top:1px solid #ddd;border-bottom:1px solid #ccc}
.main-nav ul{list-style:none;display:flex;position:absolute;left:85px;top:7px;font-family:"Ubuntu",sans-serif;font-size:10px;color:#555;letter-spacing:.3px}
.main-nav li{padding:2px 9px;margin-right:6px}
.main-nav li.active{background:#fff;border:1px solid #ccc;border-radius:10px;color:#333;box-shadow:0 1px 2px rgba(0,0,0,.15)}

/* hero */
.hero{left:0;top:103px;width:721px;height:232px;background:radial-gradient(ellipse at 60% 30%,#2d4370,var(--navy) 55%,var(--navy-deep));overflow:hidden}
.hero-floor{left:0;top:200px;width:721px;height:32px;background:linear-gradient(#111,#1c1c1c)}
.hero h1{left:85px;top:66px;font-family:"Ubuntu",sans-serif;font-weight:700;font-size:21px;color:#fff}
.hero p{left:85px;top:102px;width:225px;font-size:9.5px;line-height:13px;color:#c9d4e8}
.btn-online{left:132px;top:183px;width:125px;height:24px;border-radius:12px;background:linear-gradient(#f4f4f4,#bcbcbc);border:2px solid #777;font-family:"Ubuntu",sans-serif;font-weight:500;font-size:11px;color:#333;text-align:center;line-height:20px}
.hero-shot{left:332px;top:34px;width:300px;height:172px;background:linear-gradient(90deg,#c3141a 0%,#e8a02c 25%,#f3f0e4 55%,#dcdfe6 100%);border-radius:2px}

/* services */
.section-title{left:0;width:721px;text-align:center;font-family:"Ubuntu",sans-serif;font-weight:700;font-size:14px;color:var(--green)}
.title-rule{top:361px;height:1px;background:var(--line)}
.service{top:383px;width:80px;text-align:center}
.service-ring{width:78px;height:78px;border-radius:50%;border:4px solid #d8d8d8;background:#fff;margin:0 auto;display:flex;align-items:center;justify-content:center}
.service.on .service-ring{border-color:var(--green)}
.service-label{position:absolute;top:84px;left:-40px;width:160px;font-family:"Ubuntu",sans-serif;font-size:11px;color:#999;letter-spacing:.3px}
.service.on .service-label{color:var(--green)}
.dot-sep{top:421px;width:4px;height:4px;border-radius:50%;background:#ccc}

/* promo */
.promo{left:85px;top:506px;width:551px;height:63px;border-radius:4px;background:linear-gradient(90deg,#c90d12,#e4261c 60%,#b40b10)}
.promo-head{left:17px;top:11px;font-family:"PT Sans",sans-serif;font-style:italic;font-size:17px;color:#fff}
.promo-sub{left:17px;top:37px;font-family:"PT Sans",sans-serif;font-style:italic;font-size:9px;color:#fbe0e0}
.btn-quote{left:373px;top:14px;width:154px;height:33px;border-radius:4px;background:linear-gradient(#f69a3a,var(--orange));border:1px solid #b65a0c;font-family:"PT Sans",sans-serif;font-style:italic;font-weight:700;font-size:14px;color:#fff;line-height:31px;padding-left:10px}

/* video & testimonials */
.sub-title{font-family:"Ubuntu",sans-serif;font-weight:500;font-size:14px;color:#333}
.video{left:85px;top:618px;width:202px;height:152px;background:#000}
.video-bar{left:0;bottom:0;width:202px;height:20px;background:#111}
.testimonials{left:321px;top:618px;width:315px;height:152px;background:#fff;border:1px solid #eee}
.client{top:10px;width:140px}
.client-photo{width:44px;height:44px;background:linear-gradient(#4f6a4a,#2f3a2c)}
.client-name{position:absolute;left:54px;top:3px;font-size:9.5px;font-weight:700;color:#333}
.client-role{position:absolute;left:54px;top:18px;font-size:6.5px;line-height:8.5px;color:#777}
.client-role em{color:var(--red)}
.client-quote{position:absolute;left:0;top:57px;width:140px;font-size:7.5px;line-height:12px;color:#888;border-top:1px solid #eee;padding-top:6px}
.doctor{left:12px;top:129px;font-size:9.5px;color:#666}
.doctor-link{right:12px;top:130px;font-size:8px;color:var(--red)}

/* portfolio */
.portfolio{left:0;top:792px;width:721px;height:183px;background:linear-gradient(#555,#3c3c3c)}
.portfolio h2{left:0;top:8px;width:721px;text-align:center;font-family:"PT Sans",sans-serif;font-style:italic;font-weight:400;font-size:18px;color:#fff}
.portfolio .tag{left:0;top:33px;width:721px;text-align:center;font-family:"PT Sans",sans-serif;font-style:italic;font-size:10px;color:#ddd}
.tile{top:56px;width:182px;height:95px;overflow:hidden}
.tile-cap{left:0;bottom:0;width:182px;height:22px;background:rgba(0,0,0,.75);font-family:"PT Sans",sans-serif;font-size:10px;color:#fff;padding:5px 10px;letter-spacing:.4px}
.tile-corner{right:0;bottom:0;width:0;height:0;border-left:22px solid transparent;border-bottom:22px solid var(--red)}
.pager{top:163px;width:7px;height:7px;border-radius:50%;border:1px solid #ddd}

/* footer */
.footer{left:0;top:975px;width:721px;height:173px;background:linear-gradient(#0b111c,var(--footer))}
.texting{left:0;top:8px;width:721px;text-align:center;font-family:"PT Sans",sans-serif;font-style:italic;font-size:14px;color:#8fc447}
.texting b{color:#fff}
.phone{left:0;top:28px;width:721px;text-align:center;font-family:"PT Sans",sans-serif;font-size:17px;color:#8fc447}
.foot-title{font-family:"Arimo",sans-serif;font-weight:700;font-size:12px;color:#ccc;letter-spacing:.3px}
.foot-rule{height:1px;background:#2b3445}
.links{font-size:7.5px;line-height:14.6px;color:#8ea0c0;list-style:none}
.subscribe-text{left:412px;top:91px;width:224px;font-size:8px;line-height:12px;color:#8ea0c0}
.email{left:412px;top:126px;width:224px;height:22px;border-radius:11px;background:#fff;font-family:"PT Sans",sans-serif;font-style:italic;font-size:8px;color:#777;padding:6px 10px}
.send{left:580px;top:126px;width:56px;height:22px;border-radius:11px;background:var(--red);font-family:"PT Sans",sans-serif;font-style:italic;font-weight:700;font-size:13px;color:#fff;text-align:center;line-height:22px}
.bottom{left:0;top:1148px;width:721px;height:52px;background:var(--bottom)}
.bottom-social{top:13px;width:26px;height:26px;border-radius:50%;background:#ddd}
.copyright{right:85px;top:21px;font-size:8px;color:#8a93a6}
</style>
</head>
<body>

<header class="site-header abs">
  <nav class="top-links abs"><span>HOME</span><span>TESTIMONIALS</span><span>BLOGS</span><span class="login">LOGIN</span></nav>
  <div class="brand abs"><span class="brand-name">Plorven Studio<br>Company, Inc.</span></div>
  <a class="social abs" style="left:560px" aria-label="Social profile"></a>
  <a class="social abs" style="left:587px;background:#3aa6dc" aria-label="Social profile"></a>
  <a class="social abs" style="left:614px;background:#2f6ea3" aria-label="Social profile"></a>
</header>

<nav class="main-nav abs">
  <ul><li class="active">Mobile Marketing</li><li>Website Design</li><li>Social Media</li><li>Seo &amp; PPC</li><li>Hosting</li><li>Domains</li><li>Contacts</li></ul>
</nav>

<section class="hero abs">
  <div class="hero-floor abs"></div>
  <h1 class="abs">PLORVEN STUDIO</h1>
  <p class="abs">Whether you simply are in need of hosting, or you need full-blown site design and e-commerce solutions...</p>
  <a class="btn-online abs">Get Online Now!</a>
  <div class="hero-shot abs" role="img" aria-label="Fanned screenshots of client websites built by the studio"></div>
</section>

<h2 class="section-title abs" style="top:354px">WHAT WE DO?</h2>
<div class="title-rule abs" style="left:85px;width:214px"></div>
<div class="title-rule abs" style="left:422px;width:214px"></div>

<div class="service abs" style="left:99px"><div class="service-ring">
  <svg width="36" height="30" viewBox="0 0 36 30"><rect x="4" y="2" width="28" height="19" rx="2" fill="none" stroke="#aaa" stroke-width="2"/><rect x="1" y="23" width="34" height="4" rx="1" fill="#aaa"/><circle cx="18" cy="11.5" r="5" fill="none" stroke="#aaa" stroke-width="1.5"/></svg>
</div><div class="service-label">Website Design</div></div>
<div class="dot-sep abs" style="left:211px"></div>
<div class="service on abs" style="left:247px"><div class="service-ring">
  <svg width="34" height="30" viewBox="0 0 34 30"><rect x="2" y="18" width="6" height="10" fill="#f6a623"/><rect x="10" y="12" width="6" height="16" fill="#e94e1b"/><rect x="18" y="6" width="6" height="22" fill="#6bb52e"/><rect x="26" y="1" width="6" height="27" fill="#3e8e1f"/></svg>
</div><div class="service-label">Seo and PPC</div></div>
<div class="dot-sep abs" style="left:360px"></div>
<div class="service abs" style="left:396px"><div class="service-ring">
  <svg width="22" height="32" viewBox="0 0 22 32"><rect x="2" y="1" width="18" height="30" rx="3" fill="none" stroke="#aaa" stroke-width="2"/><rect x="5" y="5" width="12" height="19" fill="#ccc"/><circle cx="11" cy="27.5" r="1.5" fill="#aaa"/></svg>
</div><div class="service-label">Mobile Marketing</div></div>
<div class="dot-sep abs" style="left:509px"></div>
<div class="service abs" style="left:545px"><div class="service-ring">
  <svg width="34" height="30" viewBox="0 0 34 30"><rect x="6" y="2" width="22" height="16" rx="1" fill="#aaa"/><rect x="15" y="18" width="4" height="6" fill="#aaa"/><rect x="2" y="24" width="30" height="2" fill="#aaa"/><circle cx="17" cy="25" r="2.5" fill="#fff" stroke="#aaa"/></svg>
</div><div class="service-label">Hosting</div></div>

<section class="promo abs">
  <div class="promo-head abs">Get your own TextPerk Account for a 10% discount</div>
  <div class="promo-sub abs">Click Here and use Promo Code: plorvenstudio</div>
  <a class="btn-quote abs">Request a Quote
    <svg class="abs" style="right:8px;top:8px" width="16" height="16" viewBox="0 0 16 16"><path d="M3 2 L13 8 L3 14" fill="none" stroke="#ffd2a3" stroke-width="2"/></svg></a>
</section>

<h3 class="sub-title abs" style="left:85px;top:590px">Watch this Video</h3>
<div class="video abs">
  <svg class="abs" style="left:80px;top:55px" width="44" height="44" viewBox="0 0 44 44"><circle cx="22" cy="22" r="20" fill="none" stroke="#666" stroke-width="2.5"/><path d="M17 13 L31 22 L17 31Z" fill="#666"/></svg>
  <div class="video-bar abs">
    <svg class="abs" style="left:7px;top:5px" width="10" height="10"><rect x="1" width="3" height="10" fill="#fff"/><rect x="6" width="3" height="10" fill="#fff"/></svg>
    <span class="abs" style="left:25px;top:-5px;font-size:6px;color:#fff">00:00</span>
    <div class="abs" style="left:34px;top:8px;width:150px;height:4px;background:#444"></div>
    <svg class="abs" style="left:188px;top:6px" width="8" height="8"><rect width="3" height="3" fill="#fff"/><rect x="5" width="3" height="3" fill="#fff"/><rect y="5" width="3" height="3" fill="#fff"/><rect x="5" y="5" width="3" height="3" fill="#fff"/></svg>
  </div>
</div>

<h3 class="sub-title abs" style="left:321px;top:590px">What our client's say</h3>
<section class="testimonials abs">
  <div class="client abs" style="left:11px">
    <div class="client-photo" role="img" aria-label="Video thumbnail of client testimonial"></div>
    <div class="client-name">Dale Hartwick</div>
    <div class="client-role">Owner, <em>Ridgeline<br>BikeWorks.com</em></div>
    <p class="client-quote">There are many variations of passages of lorem ipsum available, but the majority have suffered alteration.</p>
  </div>
  <div class="client abs" style="left:167px">
    <div class="client-photo" role="img" aria-label="Video thumbnail of client testimonial"></div>
    <div class="client-name">Dale Hartwick</div>
    <div class="client-role">Owner, <em>Ridgeline<br>BikeWorks.com</em></div>
    <p class="client-quote">There are many variations of passages of lorem ipsum available, but the majority have suffered alteration.</p>
  </div>
  <div class="doctor abs">Are you a doctor who needs more patients?</div>
  <a class="doctor-link abs">Click here &#8857;</a>
</section>

<section class="portfolio abs">
  <h2 class="abs">From Plorven Studio, Inc. Portfolio</h2>
  <div class="tag abs">Who Trust Us (You could be here as well.)</div>
  <div class="tile abs" style="left:85px;background:linear-gradient(#f0b22a,#f6e9c8 60%,#fff)" role="img" aria-label="Bright Morning website screenshot">
    <div class="tile-cap abs">Bright Morning</div><div class="tile-corner abs"></div></div>
  <div class="tile abs" style="left:269px;background:linear-gradient(90deg,#dfe6f0,#8aa07a 60%,#c9d3db)" role="img" aria-label="Maple Hollow Inn website screenshot">
    <div class="tile-cap abs">Maple Hollow Inn</div><div class="tile-corner abs"></div></div>
  <div class="tile abs" style="left:454px;background:linear-gradient(#f2e8ea,#c79aa6 60%,#7a4a55)" role="img" aria-label="Oakvale Women's Health website screenshot">
    <div class="tile-cap abs">Oakvale Women's Health</div><div class="tile-corner abs"></div></div>
  <span class="pager abs" style="left:351px"></span><span class="pager abs" style="left:363px"></span>
</section>

<footer class="footer abs">
  <div class="texting abs">See Mobile in action by texting <b>DEMO</b> to</div>
  <div class="phone abs">123 456 7890<span style="color:#fff">*</span></div>
  <h4 class="foot-title abs" style="left:85px;top:60px">Quik Links</h4>
  <div class="foot-rule abs" style="left:85px;top:82px;width:251px"></div>
  <ul class="links abs" style="left:85px;top:91px"><li>Home</li><li>About Us</li><li>Blogs</li><li>Testimonials</li><li>Contact / RFP</li></ul>
  <ul class="links abs" style="left:179px;top:91px"><li>Mobile Marketing</li><li>Website Design</li><li>Social Media</li><li>Seo and PPC</li><li>Hosting</li></ul>
  <ul class="links abs" style="left:283px;top:91px"><li>Domains</li><li>Terms of Use</li><li>Privacy Statment</li></ul>
  <h4 class="foot-title abs" style="left:412px;top:60px">Subscribe to Our Email List</h4>
  <div class="foot-rule abs" style="left:412px;top:82px;width:224px"></div>
  <p class="subscribe-text abs">We appreciate your interest in Harrowgate Music School and glad you want to stay up to date, thanks for the support!</p>
  <div class="email abs">Enter your email</div>
  <a class="send abs">Send</a>
</footer>

<div class="bottom abs">
  <span class="bottom-social abs" style="left:85px" aria-label="Social profile"></span>
  <span class="bottom-social abs" style="left:115px" aria-label="Social profile"></span>
  <span class="bottom-social abs" style="left:145px" aria-label="Social profile"></span>
  <div class="copyright abs">Copyright &copy; 2013 Plorven Studio, Inc. All rights reserved.</div>
</div>

</body>
</html>
```